Geschäftspapiere für ein Hotel
Zielgruppe
Wir sind ein Hotel in den Tiroler Bergen im höchsten Wintersportort Österreichs - in Kühtai.
Aufgabenstellung
Wir hättn gerne neue Kuverts...
einmal im Format C6/5 (ohne Adress-Fenster)
und dann noch im Format C4 und
dann noch Briefpapier
Wir haben neben unserem Hotel noch ein kleines Häuschen mit Ferienwohnungen...das Logo ist auch bei den Dateien.
Noch dazu haben wir ein Restaurant im Haus....Logo ist auch dabei.
Noch dazu ist ein Foto bei den Dateien welches in Österreich auf jedem Kuvert sein muss.
Einige Bilder von unserem Haus und Wellness-Bereich hab ich auch noch hinzugefügt.
Freue mich auf viele Design-Vorschläge
Unter folgendem Link werde ich heute nachmittag noch einige Fotos uploaden:
https://ablage.wolkenfach-net.de/ordner/7pQmz3RtX9vLk2nBw4sYdHfJc8aEuGo?zugang=offen

```html
<!DOCTYPE html>
<html lang="de">
<head>
<meta charset="utf-8">
<title>Sonnwiesen Residenz – Briefpapier</title>
<link href="https://fonts.googleapis.com/css2?family=Source+Sans+3:wght@400;600&display=swap" rel="stylesheet">
<style>
  :root {
    --paper: #ffffff;
    --brand-brown: #5b4034;
    --brand-brown-light: #7a5a4a;
    --text-grey: #4f4a47;
    --icon-grey: #5a5350;
    --snow-top: #eef1f5;
    --snow-mid: #f4f6f9;
  }
  * { margin: 0; padding: 0; box-sizing: border-box; }
  html, body { width: 848px; height: 1200px; overflow: hidden; background: var(--paper); }
  body { font-family: "Source Sans 3", Arial, sans-serif; color: var(--text-grey); }

  .letterhead { position: relative; width: 848px; height: 1200px; background: var(--paper); }

  .header-scenery {
    position: absolute; left: 0; top: 0; width: 848px; height: 340px;
    background:
      linear-gradient(180deg, rgba(255,255,255,0) 55%, var(--paper) 100%),
      linear-gradient(170deg, var(--snow-top) 0%, #e3e7ed 30%, var(--snow-mid) 60%, var(--paper) 100%);
  }

  .brand-name {
    position: absolute; left: 640px; top: 76px; width: 150px;
    text-align: center;
    font-size: 21px; font-weight: 600; letter-spacing: 0.5px;
    color: var(--brand-brown); line-height: 1.15;
  }

  .address {
    position: absolute; left: 670px; top: 153px;
    font-size: 12px; line-height: 18.5px; color: var(--text-grey);
    font-style: normal;
  }

  .contact-list { position: absolute; left: 646px; top: 215px; list-style: none; }
  .contact-list li {
    display: flex; align-items: center; height: 23.5px;
    font-size: 12px; color: var(--text-grey);
  }
  .contact-list svg { width: 15px; height: 15px; margin-right: 9px; flex: none; }

  .footer-rule-top {
    position: absolute; left: 0; top: 1034px; width: 848px; height: 5px;
    background: var(--brand-brown);
  }
  .footer-rule-bottom {
    position: absolute; left: 0; top: 1166px; width: 848px; height: 4px;
    background: var(--brand-brown-light);
  }

  .photo-strip { position: absolute; left: 0; top: 1046px; width: 848px; height: 109px; }
  .photo { position: absolute; top: 0; height: 109px; width: 164px; }
  .photo--mountains { left: 0;   background: linear-gradient(180deg, #3f6da8 0%, #8fb0d6 45%, #eef2f7 75%, #d7dee8 100%); }
  .photo--hotel     { left: 171px; background: linear-gradient(180deg, #6d95c9 0%, #c9d7e6 40%, #a4504a 65%, #f1f1f1 100%); }
  .photo--pool      { left: 342px; background: linear-gradient(180deg, #1c2a52 0%, #3b5f9c 35%, #5fb3e6 70%, #a7dcf5 100%); }
  .photo--restaurant{ left: 513px; background: linear-gradient(180deg, #6b4a36 0%, #b78a62 40%, #d9b58c 70%, #8d6447 100%); }
  .photo--room      { left: 684px; background: linear-gradient(180deg, #a8795a 0%, #c99c74 40%, #f0e6dd 70%, #b0372f 100%); }
</style>
</head>
<body>
<main class="letterhead">
  <div class="header-scenery" role="img" aria-label="Verblasste verschneite Berglandschaft als Kopfhintergrund"></div>

  <div class="brand-name">Sonnwiesen<br>Residenz</div>

  <address class="address">
    Sonnwiesen Residenz<br>
    Almweg 14<br>
    6190 Hochtal
  </address>

  <ul class="contact-list">
    <li>
      <svg viewBox="0 0 16 16" aria-hidden="true"><circle cx="8" cy="8" r="8" fill="var(--icon-grey)"/><path d="M5.2 4.2l1.4-.4.9 2-1 .8a5 5 0 0 0 2.9 2.9l.8-1 2 .9-.4 1.4c-3.6.2-6.8-3-6.6-6.6z" fill="#fff"/></svg>
      +43 (0) 5120 4471
    </li>
    <li>
      <svg viewBox="0 0 16 16" aria-hidden="true"><circle cx="8" cy="8" r="8" fill="var(--icon-grey)"/><rect x="4" y="5.2" width="8" height="5.6" rx="0.6" fill="#fff"/><path d="M4.3 5.6L8 8.4l3.7-2.8" fill="none" stroke="var(--icon-grey)" stroke-width="0.9"/></svg>
      info@sonnwiesen.at
    </li>
    <li>
      <svg viewBox="0 0 16 16" aria-hidden="true"><circle cx="8" cy="8" r="8" fill="var(--icon-grey)"/><circle cx="8" cy="8" r="4" fill="none" stroke="#fff" stroke-width="0.9"/><ellipse cx="8" cy="8" rx="1.8" ry="4" fill="none" stroke="#fff" stroke-width="0.8"/><path d="M4 8h8" stroke="#fff" stroke-width="0.8"/></svg>
      www.sonnwiesen.at
    </li>
  </ul>

  <div class="footer-rule-top"></div>
  <div class="photo-strip">
    <div class="photo photo--mountains" role="img" aria-label="Verschneite Berggipfel unter blauem Himmel"></div>
    <div class="photo photo--hotel" role="img" aria-label="Hotelgebäude im Winter vor Bergkulisse"></div>
    <div class="photo photo--pool" role="img" aria-label="Beleuchtetes Hallenbad im Wellnessbereich"></div>
    <div class="photo photo--restaurant" role="img" aria-label="Restaurant mit Holzeinrichtung und gedeckten Tischen"></div>
    <div class="photo photo--room" role="img" aria-label="Gästezimmer mit Doppelbett und roten Kissen"></div>
  </div>
  <div class="footer-rule-bottom"></div>
</main>
</body>
</html>
```